WIX Landing Page for Cosmetic Distributor

We want to relaunch our current website (dravolin.ch), and are looking for a template from you on WIX. We are a distributor of chemical raw materials for beauty products. Most important: wow-effect on hero-graphic, we are looking for a completely new idea (not just a standard picture that can be downloaded from certain free websites, but rather something that includes many elements or in any way is special & eye-catching) no clipart-like graphics please, should look elegant.
• Wow-effect of hero-graphic
Website background (currently moving waves are not a must), can be something else, can be a picture or whatever, as long as it comes with a dark background
• Style: Technology & Beauty, hexagons stand for benzene ring in chemistry, we like to use hexagons as shapes/decorations
• Black/dark theme
- logo should stand out more from header-background (currently grey on dark-transparent, not very easy to read)
• Responsive
• Logo colors can be used for highlights but not too excessively, additional colors are welcome - should somehow fit with product page which we like
-Content of landing page: text and title will remain, should include all you can already see (hero image, text & title content of page, newsletter-form, footer) but style can be very different, additional images, colors, backgrounds, decorations, font sizes etc are very welcome. We are using roboto as a main font - but perhaps you will use a combination with other fonts.
• Please change the 6 tiles (logistik etc), not happy & too overloaded. Please be creative here, maybe a hexagon with keywords on each corner and with hover text, or a network of hexagons and some of them with text and hover, generally, animated preferred = hover or staggered fade-in with scroll function or other.
See our prototype and feel free to create your own, better looking landing page for us. We would like you to create a template in WIX that we can use. You can copy our prototype to have a point to start with.
Prototype: https://studio318907.wixsite.com/dravolin
Target Market(s)
Cosmetic Industry Switzerland, Austria, Germany
Industry/Entity Type
cosmetic raw matierials industry (technical, beauty)
Number of Pages Required
1 page
Font styles to use
Other font styles liked:
- Roboto
Requirements
Must have
- hero-image, eye-catching

```html
<!DOCTYPE html>
<html lang="en">
<head>
<meta charset="utf-8">
<title>Dravolin – Creative Chemicals</title>
<link rel="stylesheet" href="https://fonts.googleapis.com/css2?family=Rubik:wght@500;700&family=Roboto:wght@400;500;700&display=swap">
<style>
:root{
  --navy-deep:#081729;
  --navy:#0b223d;
  --topbar:#0d2c54;
  --band:#0e3766;
  --accent:#2d84c6;
  --orange:#ef7d17;
  --hex-title:#5f9bd6;
  --muted:#b7c3d2;
  --white:#ffffff;
  --ink:#1c2633;
}
*{box-sizing:border-box;margin:0;padding:0}
html,body{width:1200px;height:3975px;overflow:hidden;background:var(--navy-deep)}
body{font-family:"Roboto",Arial,sans-serif;color:var(--white);position:relative}
.abs{position:absolute}
.head{font-family:"Rubik",Arial,sans-serif;font-weight:700;text-transform:uppercase;letter-spacing:1px}

/* top bar */
.topbar{left:0;top:0;width:1200px;height:51px;background:var(--topbar);font-size:20px;font-weight:500}
.topbar .connect{left:45px;top:13px}
.topbar .social{top:7px;width:36px;height:36px;border-radius:50%}
.topbar .lang{left:794px;top:13px}
.topbar .phone{right:51px;top:13px;display:flex;gap:10px;align-items:center}

/* nav */
.nav{left:0;top:51px;width:1200px;height:83px;background:var(--white)}
.brand{left:48px;top:20px;display:flex;align-items:center;gap:12px;color:var(--accent);font-size:38px;font-weight:400}
.brand-dot{width:34px;height:34px;border-radius:50%;background:var(--accent)}
.nav a{position:absolute;top:28px;color:var(--ink);font-size:21px;text-decoration:none;font-weight:500}

/* hero */
.hero{left:0;top:134px;width:1200px;height:560px;background:var(--navy-deep);overflow:hidden}
.hero-photo{left:447px;top:0;width:753px;height:560px;background:radial-gradient(ellipse at 60% 45%,#c9957a 0%,#8a5a44 25%,#1f3f2c 55%,#1e5a9a 80%,#0c2c5a 100%)}
.hero-kicker{left:45px;top:168px;color:var(--orange);font-size:24px}
.hero-title{left:45px;top:210px;font-size:52px;line-height:68px}
.btn-outline{display:flex;align-items:center;justify-content:center;border:3px solid var(--white);color:var(--white);font-family:"Rubik",Arial,sans-serif;font-weight:700;font-size:21px;text-transform:uppercase;letter-spacing:.5px}
.hero .btn-outline{left:45px;top:366px;width:268px;height:72px}

/* services */
.services{left:0;top:694px;width:1200px;height:969px;background:var(--navy)}
.frame-title{left:177px;top:116px;width:847px;height:208px;text-align:center;font-size:42px;line-height:57px;padding-top:16px}
.rule{height:2px;background:var(--muted);opacity:.6}
.dot{width:12px;height:12px;border-radius:50%;background:var(--orange)}
.hex-text{width:220px;text-align:center}
.hex-text h3{font-family:"Rubik",Arial,sans-serif;font-weight:700;text-transform:uppercase;color:var(--hex-title);font-size:23px;line-height:31px;letter-spacing:1px;margin-bottom:8px}
.hex-text p{font-size:20px;line-height:23px;color:var(--muted)}
.hex-text.active h3,.hex-text.active p{color:var(--white)}

/* blog */
.blog{left:0;top:1663px;width:1200px;height:885px;background:var(--band)}
.blog-title{left:0;top:72px;width:1200px;text-align:center;font-size:44px;line-height:58px}
.blog-intro{left:66px;top:205px;width:1068px;text-align:center;font-size:20px;line-height:34px}
.card{top:387px;width:349px;height:310px;background:var(--navy)}
.card-img{left:0;top:0;width:349px;height:203px}
.card-date{left:0;top:169px}
.card-date span{position:absolute;left:0;top:16px;width:88px;text-align:center;font-family:"Rubik",Arial,sans-serif;font-weight:700;font-size:19px;line-height:21px}
.card h4{position:absolute;left:87px;top:218px;font-size:20px;font-weight:400}
.card a{position:absolute;left:87px;top:254px;font-family:"Rubik",Arial,sans-serif;font-weight:700;font-size:19px;color:var(--white)}
.blog .btn-cut{left:449px;top:728px}

/* partners */
.partners{left:0;top:2548px;width:1200px;height:830px;background:var(--navy-deep)}
.partners h2{left:0;top:80px;width:1200px;text-align:center;font-size:44px}
.pill{width:271px;height:92px;border-radius:46px;background:#12253f;display:flex;align-items:center;justify-content:center}
.pill.light{background:var(--white)}
.pill i{display:block;width:150px;height:30px;border-radius:15px;background:#2a3b52}
.pill.light i{background:#d8dde4}
.slider-dot{top:434px;width:15px;height:15px;border:2px solid var(--white)}

/* newsletter */
.news{left:139px;top:487px;width:924px;height:286px;background:var(--accent);border-radius:90px 0 0 0}
.news-frame{left:38px;top:51px;width:847px;height:181px;border:6px solid var(--white)}
.news h2{left:170px;top:32px;width:584px;text-align:center;background:var(--accent);font-size:44px}
.news p{left:120px;top:98px;width:684px;text-align:center;font-size:20px;line-height:34px}
.btn-sub{left:310px;top:198px;width:304px;height:72px;background:var(--orange);display:flex;align-items:center;justify-content:center;font-family:"Rubik",Arial,sans-serif;font-weight:700;font-size:21px;letter-spacing:.5px}

/* footer */
.footer{left:0;top:3378px;width:1200px;height:571px;background:var(--navy-deep)}
.footer h5{font-family:"Roboto",Arial,sans-serif;font-weight:500;font-size:24px;text-transform:uppercase}
.footer ul{list-style:none;font-size:21px}
.footer li{height:48.6px}
.bullets li{padding-left:28px;position:relative}
.bullets li::before{content:"";position:absolute;left:0;top:11px;width:8px;height:8px;border-radius:50%;background:var(--orange)}
.contact-row{display:flex;gap:14px;font-size:21px;line-height:31px}
.contact-row svg{flex:none;margin-top:5px}
.bottombar{left:0;top:3949px;width:1200px;height:26px;background:var(--band);font-size:19px;line-height:26px}
</style>
</head>
<body>

<header class="abs topbar">
  <span class="abs connect">Connect With Us</span>
  <span class="abs social" style="left:230px;background:var(--orange)"></span>
  <span class="abs social" style="left:277px;background:#6e93c4"></span>
  <span class="abs social" style="left:323px;background:#6e93c4"></span>
  <span class="abs lang">EN ▾</span>
  <span class="abs phone">
    <svg width="20" height="20" viewBox="0 0 24 24"><path fill="#ef7d17" d="M6.6 10.8a15 15 0 0 0 6.6 6.6l2.2-2.2c.3-.3.7-.4 1-.2 1.1.4 2.3.6 3.6.6.6 0 1 .4 1 1V20c0 .6-.4 1-1 1A17 17 0 0 1 3 4c0-.6.4-1 1-1h3.5c.6 0 1 .4 1 1 0 1.3.2 2.5.6 3.6.1.3 0 .7-.2 1z"/></svg>
    +41 44 555 01 20
  </span>
</header>

<nav class="abs nav">
  <div class="abs brand"><span class="brand-dot"></span>Dravolin</div>
  <a href="#" style="left:676px">Home</a>
  <a href="#" style="left:801px">Products</a>
  <a href="#" style="left:959px">Blog</a>
  <a href="#" style="left:1071px">Contact</a>
</nav>

<section class="abs hero">
  <div class="abs hero-photo" role="img" aria-label="Beauty portrait with a yellow orchid and tropical palm leaves against a blue backdrop"></div>
  <p class="abs head hero-kicker">We sell chemicals</p>
  <h1 class="abs head hero-title">We care about<br>you</h1>
  <a class="abs btn-outline" href="#">Get started now</a>
  <div class="abs rule" style="left:0;top:558px;width:1200px;opacity:.25"></div>
  <svg class="abs" style="left:518px;top:490px" width="160" height="70" viewBox="0 0 160 70">
    <polygon points="56,0 112,0 112,0" fill="none"/>
    <polygon points="56,0 110,32 110,96 56,128 2,96 2,32" transform="scale(.55) translate(0,0)" fill="#1f63b0"/>
    <polygon points="134,38 154,38 164,55 154,72 134,72 124,55" fill="var(--orange)" transform="translate(-10,-20)"/>
  </svg>
</section>

<section class="abs services">
  <div class="abs rule" style="left:0;top:216px;width:177px"></div>
  <div class="abs dot" style="left:83px;top:211px"></div>
  <div class="abs rule" style="left:1024px;top:216px;width:176px"></div>
  <div class="abs dot" style="left:1089px;top:211px"></div>

  <svg class="abs" style="left:177px;top:116px" width="847" height="208" viewBox="0 0 847 208">
    <path d="M78 3H3v202h78M769 3h75v202h-78" fill="none" stroke="#fff" stroke-width="6"/>
  </svg>
  <h2 class="abs head frame-title">Creative raw materials<br>for the personal care and home<br>care industry</h2>

  <svg class="abs" style="left:0;top:0" width="1200" height="969" viewBox="0 0 1200 969">
    <defs>
      <linearGradient id="logistics-fill" x1="0" y1="0" x2="1" y2="1">
        <stop offset="0" stop-color="#f29a3a"/><stop offset="1" stop-color="#d8660c"/>
      </linearGradient>
    </defs>
    <g fill="none" stroke="#2e4563" stroke-width="2">
      <polygon points="318,328 450,404 450,556 318,632 186,556 186,404"/>
      <polygon points="881,328 1013,404 1013,556 881,632 749,556 749,404"/>
      <polygon points="319,598 451,674 451,826 319,902 187,826 187,674"/>
      <polygon points="600,598 732,674 732,826 600,902 468,826 468,674"/>
      <polygon points="884,598 1016,674 1016,826 884,902 752,826 752,674"/>
    </g>
    <polygon points="602,328 734,404 734,556 602,632 470,556 470,404" fill="url(#logistics-fill)" stroke="#fff" stroke-width="4" role="img" aria-label="Warehouse shelves with stacked containers"/>
  </svg>

  <div class="abs hex-text" style="left:208px;top:384px"><h3>Project<br>support</h3><p>Tailor-made solutions, meaningful documents and studies, fast sampling.</p></div>
  <div class="abs hex-text active" style="left:492px;top:416px"><h3>Logistics</h3><p>Own raw materials warehouse with optimal availability and fast delivery service.</p></div>
  <div class="abs hex-text" style="left:771px;top:384px"><h3>Know-how<br>transfer</h3><p>We deliver new ideas and trends for successful and innovative projects.</p></div>
  <div class="abs hex-text" style="left:209px;top:654px"><h3>Customer<br>focus</h3><p>As the first point of contact for inquiries, we offer you the best solution.</p></div>
  <div class="abs hex-text" style="left:490px;top:684px"><h3>Reachability</h3><p>Our attentive team is within reach and will be at your disposal quickly.</p></div>
  <div class="abs hex-text" style="left:774px;top:684px"><h3>Competence</h3><p>Our many years of experience enable us to provide a comprehensive consulting service.</p></div>
</section>

<section class="abs blog">
  <h2 class="abs head blog-title">Blog –<br>Trends &amp; things worth knowing</h2>
  <p class="abs blog-intro">A timely exchange of knowledge is the focus for us and our customers and is of central importance for a successful, sustainable business relationship. Find out more about our latest active ingredients and functional raw materials here. In addition to innovative products, we present current concepts, marketing information and trends in the field of cosmetics.</p>

  <article class="abs card" style="left:45px">
    <div class="abs card-img" role="img" aria-label="Woman among white spring flowers under a blue sky" style="background:linear-gradient(180deg,#5d93c9 0%,#a8c6dd 55%,#d9d6c7 80%,#6d5a8a 100%)"></div>
    <div class="abs card-date"><svg width="88" height="76" viewBox="0 0 88 76"><polygon points="22,0 66,0 88,38 66,76 22,76 0,38" fill="var(--orange)"/></svg><span>08FEB<br>2022</span></div>
    <h4>Anti-glycation potential</h4><a href="#">READ MORE</a>
  </article>
  <article class="abs card" style="left:424px">
    <div class="abs card-img" role="img" aria-label="Woman with flowing hair in front of a mountain lake" style="background:linear-gradient(180deg,#8fb6da 0%,#c9d9e6 45%,#6f8eaa 75%,#2f5577 100%)"></div>
    <div class="abs card-date"><svg width="88" height="76" viewBox="0 0 88 76"><polygon points="22,0 66,0 88,38 66,76 22,76 0,38" fill="var(--orange)"/></svg><span>02AUG<br>2022</span></div>
    <h4>Less hair loss and gray hair</h4><a href="#">READ MORE</a>
  </article>
  <article class="abs card" style="left:804px">
    <div class="abs card-img" role="img" aria-label="Person splashing through turquoise sea water" style="background:linear-gradient(180deg,#2e7f93 0%,#4aa2b3 40%,#cfe6ec 75%,#ffffff 100%)"></div>
    <div class="abs card-date"><svg width="88" height="76" viewBox="0 0 88 76"><polygon points="22,0 66,0 88,38 66,76 22,76 0,38" fill="var(--orange)"/></svg><span>08FEB<br>2022</span></div>
    <h4>Hydrated and toned skin</h4><a href="#">READ MORE</a>
  </article>

  <a class="abs btn-cut" href="#" style="width:304px;height:74px">
    <svg class="abs" style="left:0;top:0" width="304" height="74" viewBox="0 0 304 74"><path d="M40 1.5H302.5V72.5H1.5V30z" fill="none" stroke="#fff" stroke-width="3"/></svg>
    <span class="abs head" style="left:0;top:24px;width:304px;text-align:center;font-size:21px;letter-spacing:.5px;color:#fff">View all blog post</span>
  </a>
</section>

<section class="abs partners">
  <h2 class="abs head">Our delivery partners</h2>
  <div class="abs pill" style="left:187px;top:181px"><i></i></div>
  <div class="abs pill" style="left:464px;top:181px"><i></i></div>
  <div class="abs pill light" style="left:742px;top:181px"><i></i></div>
  <div class="abs pill" style="left:187px;top:295px"><i></i></div>
  <div class="abs pill" style="left:464px;top:295px"><i></i></div>
  <div class="abs pill" style="left:742px;top:295px"><i></i></div>
  <div class="abs slider-dot" style="left:564px;background:var(--orange);border-color:var(--orange)"></div>
  <div class="abs slider-dot" style="left:592px"></div>
  <div class="abs slider-dot" style="left:620px"></div>

  <div class="abs rule" style="left:0;top:625px;width:177px"></div>
  <div class="abs dot" style="left:83px;top:620px"></div>
  <div class="abs rule" style="left:1024px;top:625px;width:176px"></div>
  <div class="abs dot" style="left:1089px;top:620px"></div>

  <div class="abs news">
    <div class="abs news-frame"></div>
    <h2 class="abs head">Newsletter sign up</h2>
    <p class="abs">Receive timely information about new products Track valuable regulatory leads Be inspired by our ideas</p>
    <a class="abs btn-sub" href="#">SUBSCRIBE NOW</a>
  </div>
</section>

<footer class="abs footer">
  <h5 class="abs" style="left:43px;top:30px">Registered office</h5>
  <ul class="abs" style="left:43px;top:88px">
    <li>Home</li><li>Products</li><li>Blog</li><li>Contact</li>
  </ul>

  <h5 class="abs" style="left:339px;top:30px">Registered office</h5>
  <ul class="abs bullets" style="left:339px;top:88px">
    <li>Sunscreen Filter</li><li>Active Ingredients</li><li>Alpine Bioactive</li><li>Vitamins</li>
    <li>Surfactants &amp; Emulsifiers</li><li>Oils &amp; oil components</li><li>Texture additives &amp; exfoliating body</li><li>More specialties</li>
  </ul>

  <h5 class="abs" style="left:774px;top:30px">Registered office</h5>
  <div class="abs contact-row" style="left:774px;top:88px;width:400px">
    <svg width="20" height="24" viewBox="0 0 20 24"><path fill="#ef7d17" d="M10 0a8 8 0 0 0-8 8c0 6 8 16 8 16s8-10 8-16a8 8 0 0 0-8-8zm0 11a3 3 0 1 1 0-6 3 3 0 0 1 0 6z"/></svg>
    <span>DRAVOLIN GmbH Lindenweg 14 CH-8600 Talwil</span>
  </div>
  <div class="abs contact-row" style="left:774px;top:164px">
    <svg width="20" height="20" viewBox="0 0 24 24"><path fill="#ef7d17" d="M6.6 10.8a15 15 0 0 0 6.6 6.6l2.2-2.2c.3-.3.7-.4 1-.2 1.1.4 2.3.6 3.6.6.6 0 1 .4 1 1V20c0 .6-.4 1-1 1A17 17 0 0 1 3 4c0-.6.4-1 1-1h3.5c.6 0 1 .4 1 1 0 1.3.2 2.5.6 3.6.1.3 0 .7-.2 1z"/></svg>
    <span>+41 44 555 01 20</span>
  </div>
  <div class="abs contact-row" style="left:774px;top:208px">
    <svg width="20" height="16" viewBox="0 0 20 16"><rect x="0" y="0" width="20" height="16" rx="2" fill="#ef7d17"/><path d="M1 2l9 7 9-7" fill="none" stroke="#081729" stroke-width="1.6"/></svg>
    <span>info@dravolin.ch</span>
  </div>

  <h5 class="abs" style="left:774px;top:296px">Warehousing and logistics</h5>
  <div class="abs contact-row" style="left:774px;top:352px;width:380px">
    <svg width="20" height="24" viewBox="0 0 20 24"><path fill="#ef7d17" d="M10 0a8 8 0 0 0-8 8c0 6 8 16 8 16s8-10 8-16a8 8 0 0 0-8-8zm0 11a3 3 0 1 1 0-6 3 3 0 0 1 0 6z"/></svg>
    <span>Seefeldweg 9 CH-8700 Rosenau</span>
  </div>
  <div class="abs contact-row" style="left:774px;top:418px">
    <svg width="20" height="20" viewBox="0 0 24 24"><path fill="#ef7d17" d="M6.6 10.8a15 15 0 0 0 6.6 6.6l2.2-2.2c.3-.3.7-.4 1-.2 1.1.4 2.3.6 3.6.6.6 0 1 .4 1 1V20c0 .6-.4 1-1 1A17 17 0 0 1 3 4c0-.6.4-1 1-1h3.5c.6 0 1 .4 1 1 0 1.3.2 2.5.6 3.6.1.3 0 .7-.2 1z"/></svg>
    <span>+41 55 555 07 42</span>
  </div>
</footer>

<div class="abs bottombar">
  <span class="abs" style="left:45px">© 2022 <b>DRAVOLIN CREATIVECHEMICALS</b>,All right reserved</span>
  <span class="abs" style="left:977px">imprint</span>
  <span class="abs" style="left:1080px">privacy</span>
</div>

</body>
</html>
```